Home Page Design

Please see design brief attached. Concept here: sketchboard[dot]io/file/qWm83LzpR7cvXuNtYa2KhE/Brindlemoor---Landing-Page?node-id=0%3A1&t=PKr92mvnQsD4xTcZ-1

Industry/Entity Type

Wedding

Number of Pages Required

1 page

Font styles to use
Serif
Sans Serif
Decorative
Script

Colors
A7469A
B969AE
D3A5CF
EDDBEB
F8F0F9
6B429C
8869AF
B7A5CE
E3DAEB
F3F0F8

Requirements
Must have
• Please see attached PDF
Nice to have
• Please see attached PDF
Should not have
• Please see attached PDF

```html
<!DOCTYPE html>
<html lang="en">
<head>
<meta charset="utf-8">
<title>Brindlemoor — Meet Your Wedding Vendor Team</title>
<link href="https://fonts.googleapis.com/css2?family=Roboto+Slab:wght@300;400;500;700&family=Great+Vibes&family=Kaushan+Script&display=swap" rel="stylesheet">
<style>
:root{
  --purple:#7b1f86;
  --pink:#e5197f;
  --ink:#1f1f1f;
  --text:#3a3a3a;
  --muted:#777;
  --soft:#f4f3f4;
  --line:#e6e6e6;
  --white:#fff;
}
*{box-sizing:border-box;margin:0;padding:0}
html,body{width:1200px;height:3690px;overflow:hidden}
body{position:relative;font-family:"Roboto Slab",Georgia,serif;color:var(--text);background:var(--white);font-size:14px}
.abs{position:absolute}
.script{font-family:"Great Vibes",cursive;color:var(--pink);font-weight:400}
.btn{position:absolute;display:flex;align-items:center;justify-content:center;color:#fff;font-size:13px;border-radius:2px;white-space:nowrap}
.btn-purple{background:var(--purple)}
.btn-pink{background:var(--pink)}

/* top bar */
.topbar{left:0;top:0;width:1200px;height:32px;background:var(--purple);color:#fff;font-size:13px}
.topbar .item{position:absolute;top:8px;display:flex;align-items:center;gap:7px;white-space:nowrap}
.social{position:absolute;top:0;width:34px;height:32px;display:flex;align-items:center;justify-content:center}
.social.active{background:var(--pink)}
.social span{width:9px;height:9px;border-radius:50%;background:var(--pink)}
.social.active span{background:#fff}

/* header */
.header{left:0;top:32px;width:1200px;height:79px;background:#fff}
.brand{left:126px;top:52px;display:flex;align-items:center;gap:10px;font-size:28px;color:var(--purple);font-weight:400;white-space:nowrap}
.brand-mark{width:12px;height:12px;background:var(--pink)}
.nav{top:62px;font-size:14px;color:var(--ink)}

/* hero */
.hero{left:0;top:111px;width:1200px;height:540px;background:radial-gradient(ellipse at 55% 35%,#d9c7be 0%,#a88d86 30%,#6f5f5c 60%,#3f4a3d 100%);overflow:hidden}
.hero-title{left:0;width:1200px;top:380px;text-align:center;font-family:"Kaushan Script",cursive;font-size:38px;line-height:48px;color:#fff}
.hero-sub{left:0;width:1200px;top:431px;text-align:center;color:#fff;font-size:13.5px}
.select{top:468px;height:32px;background:#fff;border-radius:2px;font-size:11px;color:#666;padding:9px 12px}
.select:after{content:"";position:absolute;right:12px;top:14px;border:4px solid transparent;border-top-color:var(--pink)}
.dot{width:12px;height:12px;border:1.5px solid #fff;border-radius:50%}
.dot.on{background:var(--pink);border-color:var(--pink)}

/* categories */
.cat{top:714px;width:152px;height:152px;text-align:center;border-right:1px solid var(--line)}
.cat.active{background:#fff;box-shadow:0 3px 14px rgba(0,0,0,.1);border-right:none}
.cat svg{position:absolute;left:50%;top:38px;transform:translateX(-50%)}
.cat .label{position:absolute;left:0;right:0;top:100px;font-size:13.5px;color:var(--ink)}

/* section titles */
.title{display:flex;align-items:center;justify-content:center;gap:18px;font-size:46px;line-height:60px;white-space:nowrap}
.title-rule{position:relative;height:1px;width:42px;background:var(--pink);flex:none}
.title-rule.l:after,.title-rule.r:after{content:"";position:absolute;top:-2px;width:5px;height:5px;border-radius:50%;background:var(--pink)}
.title-rule.l:after{right:0}
.title-rule.r:after{left:0}

/* featured */
.card{top:1093px;width:296px;height:379px;background:#fff;box-shadow:0 2px 8px rgba(0,0,0,.08)}
.card .photo{position:absolute;left:0;top:0;width:296px;height:183px}
.card .rating{position:absolute;left:29px;top:188px;display:flex;align-items:center;gap:8px;font-size:12px;color:var(--ink);white-space:nowrap}
.badge{background:var(--purple);color:#fff;border-radius:9px;padding:1px 10px;font-size:11px}
.card h3{position:absolute;left:29px;top:221px;font-size:15px;font-weight:400;color:var(--ink);line-height:19px;width:200px}
.card .loc{position:absolute;left:29px;top:270px;font-size:12px;color:var(--ink);display:flex;gap:6px;align-items:center}
.card .price{position:absolute;left:29px;top:301px;font-size:13px;color:var(--pink)}

/* testimonials */
.quote-icon{left:326px;top:1725px;width:58px;height:58px;border-radius:50%;background:var(--pink);display:flex;align-items:center;justify-content:center}
.t-head{left:150px;width:410px;top:1808px;text-align:center;font-size:17px;font-weight:700;color:var(--ink);line-height:24px}
.t-body{left:155px;width:400px;top:1868px;text-align:center;font-size:13px;line-height:19px;color:var(--ink)}
.t-name{left:255px;width:200px;top:1968px;text-align:center;color:var(--pink);font-size:13px}
.t-role{left:255px;width:200px;top:1986px;text-align:center;font-size:10px;color:var(--ink)}
.promo-frame{left:652px;top:1736px;width:366px;height:221px;border:1px solid rgba(255,255,255,.35)}
.promo-text{left:652px;width:366px;top:1783px;text-align:center;font-family:"Kaushan Script",cursive;color:#fff;font-size:27px;line-height:44px}

/* features */
.feat-img{left:126px;top:2241px;width:458px;height:309px;border:1px solid var(--pink);padding:3px;background:#fff}
.feat-img div{width:100%;height:100%;background:linear-gradient(180deg,#efe0f0 0%,#e7b9dc 45%,#d78fc1 62%,#6b6f4f 85%,#3f4630 100%)}
.feat-head{left:639px;top:2260px;width:440px;font-size:17px;font-weight:700;color:var(--ink);line-height:24px}
.feat-list{left:639px;top:2332px;list-style:none;font-size:13.5px;color:var(--ink)}
.feat-list li{display:flex;align-items:center;gap:10px;height:24.4px;white-space:nowrap}
.feat-list li:before{content:"➜";display:flex;align-items:center;justify-content:center;width:13px;height:13px;border-radius:50%;background:var(--pink);color:#fff;font-size:8px;flex:none}

/* how it works */
.step{top:2817px;width:212px;height:160px;text-align:center}
.step svg{position:absolute;left:50%;top:28px;transform:translateX(-50%)}
.step p{position:absolute;left:0;right:0;top:100px;font-size:13.5px;color:var(--ink);line-height:18px}
.step-line{top:2817px;width:1px;height:160px;background:var(--line)}

/* newsletter */
.news{left:163px;top:3033px;width:874px;height:127px;background:#f6f6f6}
.news h4{position:absolute;left:141px;top:40px;font-size:17px;color:var(--purple);font-weight:700;white-space:nowrap}
.news p{position:absolute;left:141px;top:64px;font-size:12px;color:var(--ink);white-space:nowrap}
.news .input{position:absolute;left:446px;top:46px;width:253px;height:36px;background:#fff;border:1px solid #ddd;font-size:12px;color:#bbb;padding:9px 13px}

/* footer */
.footer{left:0;top:3236px;width:1200px;height:411px;background:linear-gradient(180deg,#2e2b2e 0%,#3b3035 50%,#2c2a2b 100%);overflow:hidden}
.f-brand{left:517px;top:3311px;width:167px;height:90px;background:#fff;display:flex;align-items:center;justify-content:center;gap:8px;font-size:22px;color:var(--purple)}
.f-brand .brand-mark{width:9px;height:9px}
.f-col{top:3444px}
.f-col h5{font-size:14.5px;font-weight:700;color:var(--pink);margin-bottom:13px;white-space:nowrap}
.f-col li{list-style:none;color:#fff;font-size:13.5px;height:26px;white-space:nowrap}
.bottombar{left:0;top:3647px;width:1200px;height:43px;background:var(--purple);color:#fff;font-size:12.5px}
</style>
</head>
<body>

<!-- top bar -->
<div class="abs topbar">
  <div class="item" style="left:607px">
    <svg width="12" height="12" viewBox="0 0 24 24"><path d="M6.6 10.8a15 15 0 006.6 6.6l2.2-2.2a1 1 0 011-.25 11.4 11.4 0 003.6.57 1 1 0 011 1V20a1 1 0 01-1 1A17 17 0 013 4a1 1 0 011-1h3.5a1 1 0 011 1c0 1.25.2 2.45.57 3.57a1 1 0 01-.25 1z" fill="#fff"/></svg>
    +1-555-014-2290
  </div>
  <div class="item" style="left:760px">
    <svg width="13" height="11" viewBox="0 0 26 20"><rect x="1" y="1" width="24" height="18" rx="2" fill="#fff"/><path d="M1 2l12 9 12-9" stroke="var(--purple)" stroke-width="2" fill="none"/></svg>
    hello@brindlemoor.com
  </div>
  <div class="social" style="left:967px"><span></span></div>
  <div class="social active" style="left:1001px"><span></span></div>
  <div class="social" style="left:1038px"><span></span></div>
</div>

<!-- header -->
<div class="abs header"></div>
<div class="abs brand"><span class="brand-mark"></span>Brindlemoor</div>
<div class="abs nav" style="left:508px">Vendors</div>
<div class="abs nav" style="left:600px">Venues</div>
<div class="abs nav" style="left:685px">Blogs</div>
<div class="btn btn-purple" style="left:766px;top:56px;width:135px;height:31px;font-size:13.5px">Sign in or Register</div>
<div class="btn btn-pink" style="left:929px;top:56px;width:144px;height:31px;font-size:13.5px">Join as a Vendor</div>

<!-- hero -->
<div class="abs hero" role="img" aria-label="Photo of a bride with a flower crown and a groom in a suit, framed by white and purple flowers"></div>
<div class="abs hero-title">Meet Your Wedding Vendor Team.</div>
<div class="abs hero-sub">Find and book the best wedding vendors for your special day</div>
<div class="abs select" style="left:348px;width:199px">Select Vendor type</div>
<div class="abs select" style="left:556px;width:199px">Location</div>
<div class="btn btn-purple" style="left:763px;top:468px;width:96px;height:32px">Search</div>
<div class="abs dot" style="left:557px;top:555px"></div>
<div class="abs dot on" style="left:581px;top:555px"></div>
<div class="abs dot" style="left:605px;top:555px"></div>
<div class="abs dot" style="left:630px;top:555px"></div>
<svg class="abs" style="left:0;top:520px" width="1200" height="135" viewBox="0 0 1200 135">
  <polygon points="0,14 600,84 1200,14 1200,135 0,135" fill="#fff"/>
  <polygon points="390,80 600,100 810,80 600,124" fill="var(--purple)"/>
</svg>

<!-- categories -->
<div class="abs cat" style="left:125px">
  <svg width="56" height="46" viewBox="0 0 56 46" fill="none" stroke="var(--purple)" stroke-width="2.4"><rect x="3" y="10" width="50" height="33" rx="4"/><path d="M18 10l4-7h12l4 7"/><circle cx="28" cy="26" r="11"/><circle cx="28" cy="26" r="5"/></svg>
  <div class="label">Photography</div>
</div>
<div class="abs cat" style="left:283px">
  <svg width="48" height="48" viewBox="0 0 48 48" fill="none" stroke="var(--purple)" stroke-width="2.4"><path d="M6 46V18a18 18 0 0136 0v28z"/><path d="M14 46V22a10 10 0 0120 0v24"/></svg>
  <div class="label">Venues</div>
</div>
<div class="abs cat active" style="left:443px">
  <svg width="54" height="54" viewBox="0 0 54 54" fill="none" stroke="var(--pink)" stroke-width="2.4"><path d="M14 14l10 4-4 14-10-4z"/><path d="M15 30l-6 16M4 44l10 4"/><path d="M40 14l-10 4 4 14 10-4z"/><path d="M39 30l6 16M50 44l-10 4"/><path d="M27 2v6M20 5l3 5M34 5l-3 5"/></svg>
  <div class="label">Celebrants</div>
</div>
<div class="abs cat" style="left:603px">
  <svg width="34" height="48" viewBox="0 0 34 48" fill="none" stroke="var(--purple)" stroke-width="2.4"><circle cx="9" cy="8" r="6"/><circle cx="25" cy="8" r="6"/><circle cx="17" cy="14" r="6"/><path d="M8 20h18l-6 10v16h-6V30z"/></svg>
  <div class="label">Flowers</div>
</div>
<div class="abs cat" style="left:761px">
  <svg width="40" height="50" viewBox="0 0 40 50" fill="none" stroke="var(--purple)" stroke-width="2.4"><path d="M14 2v12M26 2v12M14 14h12l-2 8 14 24H2l14-24z"/></svg>
  <div class="label">Bridal Wear</div>
</div>
<div class="abs cat" style="left:921px;border-right:none">
  <svg width="50" height="46" viewBox="0 0 50 46" fill="none" stroke="var(--purple)" stroke-width="2.4"><path d="M30 8c0-4 6-4 6 0 0-4 6-4 6 0 0 4-6 8-6 8s-6-4-6-8z"/><path d="M4 32l4-10h34l4 10v8H4z"/><path d="M12 22l4-6h18l4 6"/><circle cx="13" cy="40" r="4"/><circle cx="37" cy="40" r="4"/></svg>
  <div class="label">Cars</div>
</div>

<!-- featured vendors -->
<svg class="abs" style="left:0;top:930px" width="1200" height="660" viewBox="0 0 1200 660">
  <path d="M0,60 Q300,10 600,8 Q900,10 1200,60 V600 Q900,650 600,660 H0 Z" fill="var(--soft)"/>
</svg>
<div class="abs title script" style="left:0;width:1200px;top:1010px">
  <span class="title-rule l"></span><span>Featured Vendors</span><span class="title-rule r"></span>
</div>

<div class="abs card" style="left:126px">
  <div class="photo" role="img" aria-label="Photographer taking a picture of a smiling couple outdoors" style="background:linear-gradient(135deg,#9bb07a,#d9d6cc 55%,#6e7d55)"></div>
  <div class="rating"><span class="badge">8.8</span>Excellent <span style="color:var(--muted)">(1352 Reviews)</span></div>
  <h3>Matrimony wedding photography</h3>
  <div class="loc"><svg width="8" height="11" viewBox="0 0 8 11"><path d="M4 0a4 4 0 00-4 4c0 3 4 7 4 7s4-4 4-7a4 4 0 00-4-4z" fill="var(--purple)"/><circle cx="4" cy="4" r="1.4" fill="#fff"/></svg>Location here</div>
  <div class="price">Starting Price: $2000</div>
  <div class="btn btn-purple" style="left:29px;top:332px;width:105px;height:28px">Read More</div>
</div>
<div class="abs card" style="left:451px">
  <div class="photo" role="img" aria-label="Long outdoor banquet table set with wooden chairs and flowers" style="background:linear-gradient(135deg,#4f6b3a,#c9bba3 50%,#6c5a3f)"></div>
  <div class="rating"><span class="badge">8.8</span>Excellent <span style="color:var(--muted)">(1352 Reviews)</span></div>
  <h3>Matrimony wedding photography</h3>
  <div class="loc"><svg width="8" height="11" viewBox="0 0 8 11"><path d="M4 0a4 4 0 00-4 4c0 3 4 7 4 7s4-4 4-7a4 4 0 00-4-4z" fill="var(--purple)"/><circle cx="4" cy="4" r="1.4" fill="#fff"/></svg>Location here</div>
  <div class="price">Starting Price: $2000</div>
  <div class="btn btn-purple" style="left:29px;top:332px;width:105px;height:28px">Read More</div>
</div>
<div class="abs card" style="left:770px">
  <div class="photo" role="img" aria-label="Poolside reception with white covered chairs and palm trees" style="background:linear-gradient(135deg,#5b7fa8,#b8c8e6 50%,#3f6fa6)"></div>
  <div class="rating"><span class="badge">8.8</span>Excellent <span style="color:var(--muted)">(1352 Reviews)</span></div>
  <h3>Matrimony wedding photography</h3>
  <div class="loc"><svg width="8" height="11" viewBox="0 0 8 11"><path d="M4 0a4 4 0 00-4 4c0 3 4 7 4 7s4-4 4-7a4 4 0 00-4-4z" fill="var(--purple)"/><circle cx="4" cy="4" r="1.4" fill="#fff"/></svg>Location here</div>
  <div class="price">Starting Price: $2000</div>
  <div class="btn btn-pink" style="left:29px;top:332px;width:105px;height:28px">Read More</div>
</div>

<!-- testimonials -->
<svg class="abs" style="left:600px;top:1540px" width="600" height="576" viewBox="0 0 600 576" role="img" aria-label="Warm photo of a couple holding a bouquet of pink roses">
  <defs><linearGradient id="promoBg" x1="0" y1="0" x2="1" y2="1"><stop offset="0" stop-color="#5b3a32"/><stop offset=".5" stop-color="#7a4d47"/><stop offset="1" stop-color="#4a3330"/></linearGradient></defs>
  <polygon points="0,60 600,0 600,576 0,560" fill="url(#promoBg)"/>
</svg>
<div class="abs title script" style="left:0;width:710px;top:1654px">
  <span class="title-rule l"></span><span>Testimonials</span><span class="title-rule r"></span>
</div>
<div class="abs quote-icon">
  <svg width="28" height="22" viewBox="0 0 28 22"><path d="M2 22V12C2 5 6 1 12 0v4c-3 1-5 3-5 6h5v12zM16 22V12c0-7 4-11 10-12v4c-3 1-5 3-5 6h5v12z" fill="#fff"/></svg>
</div>
<div class="abs t-head">This is a great place to consider<br>for any event</div>
<div class="abs t-body">Lorem Ipsum is simply dummy text of the printing and typesetting industry. Lorem Ipsum has been the industry's standard dummy text ever since the 1500s, when an un-known printer took...</div>
<svg class="abs" style="left:233px;top:1979px" width="12" height="18" viewBox="0 0 12 18"><path d="M10 2L3 9l7 7" stroke="var(--purple)" stroke-width="2.5" fill="none"/></svg>
<div class="abs t-name">Mara T.</div>
<div class="abs t-role">CEO, Halvern Group</div>
<svg class="abs" style="left:465px;top:1979px" width="12" height="18" viewBox="0 0 12 18"><path d="M2 2l7 7-7 7" stroke="var(--pink)" stroke-width="2.5" fill="none"/></svg>
<div class="abs promo-frame"></div>
<div class="abs promo-text">It can be Easy for you to<br>plan a Wedding with Us</div>
<div class="btn btn-purple" style="left:782px;top:1886px;width:119px;height:31px;font-size:13.5px">Get in Touch</div>

<!-- features -->
<svg class="abs" style="left:0;top:2068px" width="1200" height="610" viewBox="0 0 1200 610">
  <path d="M0,50 L600,0 L1200,50 V560 Q900,570 600,605 Q300,570 0,560 Z" fill="var(--soft)"/>
</svg>
<div class="abs title script" style="left:0;width:1200px;top:2138px">
  <span class="title-rule l"></span><span>Features / Benefits</span><span class="title-rule r"></span>
</div>
<div class="abs feat-img"><div role="img" aria-label="Wedding stage with a floral wall, pink drapes and a gold sofa"></div></div>
<div class="abs feat-head">Lorem Ipsum is simply dummy text of the print-ing and typesetting industry.</div>
<ul class="abs feat-list">
  <li>Lorem ipsum dolor sit amet, consectetur adipiscing elit.</li>
  <li>Nunc tincidunt neque ac orci ultricies porttitor.</li>
  <li>In tincidunt enim at auctor vestibulum.</li>
  <li>Ut elementum turpis interdum enim interdum, sed molestie</li>
  <li>risus fermentum.</li>
  <li>Proin posuere eros vitae sem facilisis commodo.</li>
</ul>
<div class="btn btn-pink" style="left:639px;top:2499px;width:119px;height:31px;font-size:13.5px">Get in Touch</div>

<!-- how it works -->
<div class="abs title script" style="left:0;width:1200px;top:2730px">
  <span class="title-rule l"></span><span>How It Works?</span><span class="title-rule r"></span>
</div>
<div class="abs step" style="left:177px">
  <svg width="50" height="50" viewBox="0 0 50 50" fill="none" stroke="var(--purple)" stroke-width="2.6"><circle cx="25" cy="25" r="22"/><path d="M34 16l-5 13-13 5 5-13z"/></svg>
  <p>Explore Vendors over<br>18+ Categories</p>
</div>
<div class="abs step-line" style="left:388px"></div>
<div class="abs step" style="left:388px">
  <svg width="44" height="50" viewBox="0 0 44 50" fill="none" stroke="var(--purple)" stroke-width="2.6"><path d="M30 46H6V4h24v14"/><path d="M12 14h12M12 22h12M12 30h6"/><path d="M38 22l4 4-14 14h-4v-4z"/></svg>
  <p>Send us your Desired<br>Requirements</p>
</div>
<div class="abs step-line" style="left:600px"></div>
<div class="abs step" style="left:600px">
  <svg width="52" height="40" viewBox="0 0 52 40" fill="none" stroke="var(--purple)" stroke-width="2.6"><path d="M3 3h20v20c0 8-5 14-14 14v-6c4 0 7-3 7-8H3z"/><path d="M29 3h20v20c0 8-5 14-14 14v-6c4 0 7-3 7-8H29z"/></svg>
  <p>Get a Free Quote and<br>Compare</p>
</div>
<div class="abs step-line" style="left:811px"></div>
<div class="abs step" style="left:811px">
  <svg width="50" height="50" viewBox="0 0 50 50" fill="none" stroke="var(--purple)" stroke-width="2.6"><path d="M3 3h44v9H3zM8 3v9M14 3v9M20 3v9M26 3v9M32 3v9M38 3v9M44 3v9"/><path d="M6 12v35M44 12v35M3 47h44"/><rect x="14" y="20" width="22" height="16"/><circle cx="25" cy="26" r="3"/><path d="M19 36c0-4 3-6 6-6s6 2 6 6"/></svg>
  <p>Pick Best Deal and<br>Book Vendors</p>
</div>

<!-- newsletter -->
<div class="abs news">
  <svg style="position:absolute;left:80px;top:42px" width="52" height="40" viewBox="0 0 54 42" fill="none" stroke="var(--purple)" stroke-width="2"><path d="M16 4l36 8-8 28-36-8z"/><path d="M16 4l12 20 24-12"/><path d="M2 18h10M4 24h8M6 30h6"/></svg>
  <h4>Your Success is Our Success</h4>
  <p>Subscribe and Join Our Network</p>
  <div class="input">name@email.com</div>
  <div class="btn btn-purple" style="left:699px;top:46px;width:92px;height:32px">Sign Up</div>
</div>

<!-- footer -->
<div class="abs footer" role="img" aria-label="Dark, softly lit photo of a wedding couple among flowers"></div>
<svg class="abs" style="left:0;top:3232px" width="1200" height="124" viewBox="0 0 1200 124">
  <polygon points="0,0 1200,0 1200,120 860,120 600,4 340,120 0,120" fill="#fff"/>
  <polygon points="360,64 600,4 840,64 600,22" fill="var(--purple)"/>
</svg>
<div class="abs f-brand"><span class="brand-mark"></span>Brindlemoor</div>
<div class="abs f-col" style="left:126px">
  <h5>Quick Links</h5>
  <ul><li>About Brindlemoor</li><li>Contact Us</li><li>Our Wedding Blogs</li><li>Customer FAQs</li><li>Vendor FAQs</li></ul>
</div>
<div class="abs f-col" style="left:369px">
  <h5>Our Services</h5>
  <ul><li>Wedding Photography</li><li>Bridal Makeup</li><li>Bridal Mehndi</li><li>Bridal Outfits</li><li>Rental Transportation</li></ul>
</div>
<div class="abs f-col" style="left:599px">
  <h5>Exclusive Services</h5>
  <ul><li>About Brindlemoor</li><li>Pre-Wedding Shoot</li><li>Family Makeup</li><li>Bridal Look On Rent</li><li>Luxury &amp; Vintage Cars On Rent</li></ul>
</div>
<div class="abs f-col" style="left:858px">
  <h5>Planning &amp; Inspiration</h5>
  <ul><li>Search Vendors</li><li>Destination Weddings</li><li>Submit your Wedding</li></ul>
</div>

<div class="abs bottombar">
  <div class="abs" style="left:126px;top:13px">© 2022 Brindlemoor. All Rights Reserved</div>
  <div class="social" style="left:967px;top:5px"><span></span></div>
  <div class="social active" style="left:1001px;top:0;height:43px"><span></span></div>
  <div class="social" style="left:1038px;top:5px"><span></span></div>
</div>

</body>
</html>
```